Bref créative
TMB Business Cards and Stationary
Professional
Marcus Elsby
General Manager
2716 Bellhaven Lane
Cedar Hollow, CA 93410
marcus@tobinmillbuilders.example

```html
<!DOCTYPE html>
<html lang="en">
<head>
<meta charset="utf-8">
<title>TMB Business Cards</title>
<link href="https://fonts.googleapis.com/css2?family=Roboto:wght@400;700;900&display=swap" rel="stylesheet">
<style>
  :root {
    --backdrop: #e9e6e1;
    --card-white: #ffffff;
    --green: #1f9a2e;
    --green-dark: #0f6f1c;
    --green-light: #5cc23a;
    --ink: #222222;
    --grey: #9a9a9a;
  }
  * { box-sizing: border-box; margin: 0; padding: 0; }
  html, body {
    width: 1200px; height: 763px; overflow: hidden;
    background: var(--backdrop);
    font-family: "Roboto", Arial, sans-serif;
  }
  .stage { position: relative; width: 1200px; height: 763px; }
  .card {
    position: absolute; border-radius: 12px; overflow: hidden;
    box-shadow: 0 4px 14px rgba(0,0,0,0.22);
  }

  /* front card */
  .card-front { left: 115px; top: 120px; width: 497px; height: 280px; background: var(--card-white); }
  .front-band { position: absolute; left: 0; top: 0; width: 497px; height: 280px; }
  .brand { position: absolute; display: flex; align-items: center; gap: 14px; }
  .brand-mark { width: 40px; height: 40px; border-radius: 50%; background: var(--green); }
  .brand-name { font-weight: 900; color: var(--ink); letter-spacing: 1px; }
  .card-front .brand { left: 58px; top: 42px; }
  .card-front .brand-name { font-size: 58px; }

  .person { position: absolute; left: 52px; top: 175px; color: #fff; }
  .person-name { font-size: 21px; font-weight: 700; }
  .person-title { font-size: 12px; margin-top: 2px; }
  .person-address { font-size: 12.5px; margin-top: 14px; line-height: 1.35; }

  .contacts { position: absolute; left: 262px; top: 184px; list-style: none; color: #fff; font-size: 12.5px; }
  .contacts li { display: flex; align-items: center; gap: 8px; height: 17.5px; }
  .contacts svg { width: 12px; height: 12px; fill: #fff; flex: none; }

  /* green back card */
  .card-green {
    left: 653px; top: 65px; width: 499px; height: 266px;
    background: radial-gradient(ellipse at 50% 45%, var(--green-light) 0%, var(--green) 45%, var(--green-dark) 100%);
    display: flex; align-items: center; justify-content: center;
  }
  .card-green .brand { position: static; }
  .card-green .brand-mark { background: #fff; width: 44px; height: 44px; }
  .card-green .brand-name { color: #fff; font-size: 70px; }

  /* white back card */
  .card-plain {
    left: 353px; top: 384px; width: 494px; height: 271px;
    background: radial-gradient(ellipse at 50% 40%, #ffffff 55%, #ececec 100%);
    display: flex; align-items: center; justify-content: center;
  }
  .card-plain .brand { position: static; }
  .card-plain .brand-mark { width: 44px; height: 44px; }
  .card-plain .brand-name { font-size: 70px; }
</style>
</head>
<body>
<main class="stage">

  <section class="card card-front" aria-label="Business card front">
    <svg class="front-band" viewBox="0 0 497 280" aria-hidden="true">
      <path d="M0 142 C150 118 330 112 497 92 L497 280 L0 280 Z" fill="var(--green)"/>
      <path d="M0 150 C150 126 330 120 497 100 L497 280 L0 280 Z" fill="var(--green-dark)" opacity="0.35"/>
      <path d="M0 136 C160 110 330 106 497 82" fill="none" stroke="var(--grey)" stroke-width="4" opacity="0.6"/>
    </svg>
    <div class="brand">
      <span class="brand-mark"></span>
      <span class="brand-name">TMB</span>
    </div>
    <div class="person">
      <p class="person-name">Marcus Elsby</p>
      <p class="person-title">General Manager</p>
      <p class="person-address">2716 Bellhaven Lane<br>Cedar Hollow, CA 93410</p>
    </div>
    <ul class="contacts">
      <li><svg viewBox="0 0 12 12"><path d="M2 1h3l1 3-1.5 1a7 7 0 0 0 2.5 2.5L8 6l3 1v3a1 1 0 0 1-1 1A9 9 0 0 1 1 2a1 1 0 0 1 1-1z"/></svg>805-555-0142</li>
      <li><svg viewBox="0 0 12 12"><rect x="3" y="0.5" width="6" height="11" rx="1"/></svg>805-555-0187</li>
      <li><svg viewBox="0 0 12 12"><rect x="1" y="4" width="10" height="5" rx="1"/><rect x="3" y="1" width="6" height="3"/><rect x="3" y="8" width="6" height="3"/></svg>805-555-0163</li>
      <li><svg viewBox="0 0 12 12"><path d="M1 2h10v8H1z M1 2l5 4 5-4" fill="none" stroke="#fff" stroke-width="1.4"/></svg>marcus@tobinmillbuilders.example</li>
    </ul>
  </section>

  <section class="card card-green" aria-label="Business card back, green">
    <div class="brand">
      <span class="brand-mark"></span>
      <span class="brand-name">TMB</span>
    </div>
  </section>

  <section class="card card-plain" aria-label="Business card back, white">
    <div class="brand">
      <span class="brand-mark"></span>
      <span class="brand-name">TMB</span>
    </div>
  </section>

</main>
</body>
</html>
```